Modern Professional Service Brochure for Cloud Accountants

Please see (DRAFT content RD tri-fold brochure) pdf file attached for content only! We would like a contemporary looking tri-fold brochure (example images of lumo brochure also attached) to engage with our local target market - SME's in Alexandria. This is a top line communication that covers the basics, with one section left to complete. We would like the cover to contain a vibrant business image (as per example brochure attached) and we would like to see our signature blue used as the backing if possible. Our website is a good source of information, more images can be provided on request.

Target Market(s)

Small to Medium Business Owners in Alexandria, NSW, Australia

Industry/Entity Type

Accounting

Requirements
Must have
• LOGO
• https://quorvanet.com/preview/73529/large/artwork.png?1452840189
• Hex values
• blue #009bde / rgb 0 155 222
• light grey #888888 / rgb 136 136 136
• dark grey #4a4a4a / rgb 74 74 74
• blue/grey blend #005375
• FONT Maven Pro
Nice to have
• Content Ideas
• "The ideal mix of experts utilizing the perfect combination of skills, systems and software."
• “We are Bookkeepers, Chartered Accountants and Tax Agents specialising in cloud accounting, business advice and tax under the one roof.”
Should not have
• Pages with text "Empower Your Business" must use logo without tagline.
• Reverse logo to be used on blue background only if necessary.

```html
<!DOCTYPE html>
<html lang="en">
<head>
<meta charset="utf-8">
<title>RD co. – Tri-fold Brochure</title>
<link rel="stylesheet" href="https://fonts.googleapis.com/css2?family=Maven+Pro:wght@400;500;700&display=swap">
<style>
  :root {
    --blue: #009bde;
    --sky: #4cc3ea;
    --pale-sky: #8fd8f2;
    --navy: #005375;
    --deep-blue: #1d5f99;
    --dark-grey: #4a4a4a;
    --light-grey: #888888;
    --paper: #ffffff;
    --panel-grey: #ececec;
    --backdrop: #e4e9e9;
  }
  * { box-sizing: border-box; margin: 0; padding: 0; }
  html, body { width: 1200px; height: 1000px; overflow: hidden; }
  body {
    background: var(--backdrop);
    font-family: "Maven Pro", Arial, sans-serif;
    color: var(--dark-grey);
  }
  .canvas { position: relative; width: 1200px; height: 1000px; overflow: hidden; }

  .spread {
    position: absolute; left: 270px; width: 660px; height: 467px;
    background: var(--paper);
    box-shadow: 0 4px 16px rgba(0,0,0,0.12);
    display: flex;
  }
  .spread--outside { top: 22px; }
  .spread--inside { top: 511px; }

  .panel { position: relative; width: 220px; height: 467px; overflow: hidden; }
  .panel + .panel { border-left: 1px solid rgba(0,0,0,0.06); }
  .panel__shapes { position: absolute; inset: 0; width: 220px; height: 467px; }
  .panel__content { position: absolute; }

  .heading {
    font-size: 12.5px; font-weight: 500; letter-spacing: 0.4px;
    color: var(--sky); text-transform: uppercase; margin-bottom: 5px;
  }
  .heading--dark { color: var(--navy); }
  .heading em { font-style: normal; color: var(--sky); }
  .body-copy {
    font-size: 8px; line-height: 1.38; color: #222; text-align: justify;
  }
  .body-copy p + p { margin-top: 0; }

  /* outside spread */
  .cloud-help { left: 16px; top: 30px; width: 190px; }
  .contact { left: 16px; top: 272px; width: 195px; }
  .contact__lines { font-size: 8.2px; line-height: 1.45; color: #222; }
  .cover-logo {
    left: 118px; top: 120px; display: flex; align-items: center; gap: 4px;
    font-size: 13px; font-weight: 500; color: var(--deep-blue);
  }
  .cover-logo__mark { width: 9px; height: 9px; background: var(--deep-blue); }
  .cover-title {
    left: 16px; top: 385px; width: 195px;
    font-size: 15px; font-weight: 500; line-height: 1.45;
    color: var(--deep-blue); text-transform: uppercase;
  }

  /* inside spread */
  .why { left: 14px; top: 26px; width: 195px; }
  .why__item { display: flex; gap: 6px; margin-bottom: 7px; font-size: 7.6px; line-height: 1.35; color: #333; }
  .why__item svg { flex: 0 0 12px; margin-top: 1px; }
  .services { left: 14px; top: 30px; width: 180px; }
  .services__intro { font-size: 7.6px; line-height: 1.35; color: #333; margin-bottom: 8px; }
  .service { display: flex; gap: 6px; margin-bottom: 7px; }
  .service__num { font-size: 8px; font-weight: 700; color: var(--sky); width: 12px; }
  .service__title { font-size: 7.8px; font-weight: 700; color: var(--navy); text-transform: uppercase; }
  .service__title--plain { text-transform: none; }
  .service__text { font-size: 7.6px; line-height: 1.33; color: #333; }
  .vertical { left: 16px; top: 218px; width: 192px; }
  .vertical .heading { font-size: 13px; }
</style>
</head>
<body>
<div class="canvas">

  <!-- Outside of the brochure -->
  <section class="spread spread--outside">
    <div class="panel panel--intro">
      <svg class="panel__shapes" viewBox="0 0 220 467">
        <defs>
          <linearGradient id="introPhoto" x1="0" y1="0" x2="1" y2="1">
            <stop offset="0" stop-color="#e9e4dc"/>
            <stop offset="0.55" stop-color="#c9b08c"/>
            <stop offset="1" stop-color="#2f4f7a"/>
          </linearGradient>
        </defs>
        <polygon points="0,295 110,295 220,395 220,467 0,467" fill="url(#introPhoto)" role="img" aria-label="Photo of a smiling business owner in her shop"/>
        <polygon points="0,390 60,440 0,467" fill="var(--sky)"/>
        <polygon points="150,410 200,360 200,467 150,467" fill="var(--deep-blue)"/>
        <polygon points="175,467 220,420 220,467" fill="var(--navy)"/>
      </svg>
      <div class="panel__content cloud-help">
        <h2 class="heading">The cloud can help</h2>
        <div class="body-copy">
          <p>We are Bookkeepers, Chartered Accountants and Tax Agents specialising in cloud accounting, business advice and tax under the one roof.</p>
          <p>Life can become a lot easier and less stressful for retail businesses with the help of cloud technology. Many of the manual, paper-based business tools they currently use can be replaced with online, cloud based tools that are accessible anywhere, anytime on a smartphone or tablet. This guide is designed to help kickstart this process, with marketing tips and ideas on how to tap into the retail vertical market, which is growing all the time and filled with a myriad of opportunities.</p>
        </div>
      </div>
    </div>

    <div class="panel panel--contact" style="background: linear-gradient(180deg, #f2f2f2, #dcdcdc);">
      <svg class="panel__shapes" viewBox="0 0 220 467">
        <polygon points="0,0 40,0 150,215 120,215" fill="var(--deep-blue)"/>
        <polygon points="40,0 220,0 220,160 150,215 110,150" fill="var(--sky)"/>
        <polygon points="120,0 220,0 220,60" fill="var(--pale-sky)" opacity="0.6"/>
        <polygon points="0,410 0,467 60,467" fill="var(--sky)"/>
        <polygon points="0,380 20,380 110,467 70,467" fill="var(--navy)"/>
        <polygon points="60,467 220,380 220,467" fill="var(--deep-blue)"/>
        <polygon points="120,467 220,420 220,467" fill="var(--sky)"/>
      </svg>
      <div class="panel__content contact">
        <h2 class="heading">Get in touch</h2>
        <div class="contact__lines">
          your adress, tx, USA 1200<br>
          Phone 1300 482 615<br>
          Email rdcompany.com.au<br>
          www.rdco.com
        </div>
      </div>
    </div>

    <div class="panel panel--cover">
      <svg class="panel__shapes" viewBox="0 0 220 467">
        <defs>
          <linearGradient id="coverPhoto" x1="0" y1="0" x2="1" y2="1">
            <stop offset="0" stop-color="#d9d2c6"/>
            <stop offset="0.45" stop-color="#6f7f8e"/>
            <stop offset="1" stop-color="#1e2c44"/>
          </linearGradient>
        </defs>
        <polygon points="0,0 220,0 220,150 80,340 0,360" fill="url(#coverPhoto)" role="img" aria-label="Photo of a business owner at work in her store"/>
        <polygon points="150,0 220,0 220,40" fill="var(--sky)"/>
        <polygon points="100,140 220,75 220,210" fill="var(--paper)"/>
        <polygon points="220,75 220,95 130,140 100,140" fill="var(--sky)"/>
        <polygon points="0,150 40,200 0,260" fill="var(--sky)"/>
        <polygon points="30,230 60,260 40,300" fill="var(--deep-blue)"/>
        <polygon points="220,210 220,240 90,350 80,340" fill="var(--blue)"/>
        <line x1="220" y1="250" x2="70" y2="370" stroke="#999" stroke-dasharray="3 2" stroke-width="1"/>
      </svg>
      <div class="panel__content cover-logo">
        <span class="cover-logo__mark"></span>RD co.
      </div>
      <h1 class="panel__content cover-title">Simple ideas to kickstart your marketing</h1>
    </div>
  </section>

  <!-- Inside of the brochure -->
  <section class="spread spread--inside">
    <div class="panel panel--why">
      <svg class="panel__shapes" viewBox="0 0 220 467">
        <polygon points="0,330 0,467 90,467" fill="var(--sky)"/>
        <polygon points="0,390 50,467 0,467" fill="var(--deep-blue)"/>
        <polygon points="120,467 220,360 220,467" fill="var(--blue)"/>
        <polygon points="170,467 220,410 220,467" fill="var(--navy)"/>
      </svg>
      <div class="panel__content why">
        <h2 class="heading heading--dark">Why <em>we are the best ?</em></h2>
        <div class="why__item">
          <svg width="12" height="10" viewBox="0 0 12 10"><path d="M1 8 Q5 2 10 3 M7 1 L10 3 L8 6" fill="none" stroke="var(--sky)" stroke-width="1.4"/></svg>
          <p>Your marketing success relies on your ability to communicate the benefits of your services to your prospects, in this case, people who run their own retail businesses.</p>
        </div>
        <div class="why__item">
          <svg width="12" height="10" viewBox="0 0 12 10"><path d="M1 8 Q5 2 10 3 M7 1 L10 3 L8 6" fill="none" stroke="var(--sky)" stroke-width="1.4"/></svg>
          <p>Run a themed event marketed to local retail businesses on how they can improve their systems.</p>
        </div>
        <div class="why__item">
          <svg width="12" height="10" viewBox="0 0 12 10"><path d="M1 8 Q5 2 10 3 M7 1 L10 3 L8 6" fill="none" stroke="var(--sky)" stroke-width="1.4"/></svg>
          <p>Advertise your services in relevant trade publications. In your ad, be sure to address the industry.</p>
        </div>
        <div class="why__item">
          <svg width="12" height="10" viewBox="0 0 12 10"><path d="M1 8 Q5 2 10 3 M7 1 L10 3 L8 6" fill="none" stroke="var(--sky)" stroke-width="1.4"/></svg>
          <p>Don't be afraid to ask for referrals from your current retail clients or if the store you're shopping in is using lumo.</p>
        </div>
      </div>
    </div>

    <div class="panel panel--services">
      <svg class="panel__shapes" viewBox="0 0 220 467">
        <polygon points="150,0 185,0 220,60 220,120" fill="var(--deep-blue)"/>
        <polygon points="185,0 220,0 220,60" fill="var(--sky)"/>
        <polygon points="0,400 0,467 70,467" fill="var(--blue)"/>
      </svg>
      <div class="panel__content services">
        <h2 class="heading heading--dark">Our <em>services</em></h2>
        <p class="services__intro">Chartered Accountant practice lumo Certified Advisors / Gold Partners lumo one on one training at your place or ours. lumo set up and conversions from other software done the right way.</p>
        <div class="service">
          <span class="service__num">01</span>
          <div><p class="service__title">Slow to invoice</p><p class="service__text">Ask yourself questions like: What do they struggle with? What frustrates them? What problems?</p></div>
        </div>
        <div class="service">
          <span class="service__num">02</span>
          <div><p class="service__title">Little or no computing skills</p><p class="service__text">When considering how to engage with someone in the retail industry, a little empathy goes along way.</p></div>
        </div>
        <div class="service">
          <span class="service__num">03</span>
          <div><p class="service__title">Time poor</p><p class="service__text">The lumo ecosystem is where you'll find a range of add-ons designed specifically for the retail industry.</p></div>
        </div>
        <div class="service">
          <span class="service__num">04</span>
          <div><p class="service__title service__title--plain">A messy paper-based system</p><p class="service__text">By truly understanding the vertical market you're trying to connect with, the better your chances of making a meaningful connection with your audience.</p></div>
        </div>
      </div>
    </div>

    <div class="panel panel--vertical">
      <svg class="panel__shapes" viewBox="0 0 220 467">
        <defs>
          <linearGradient id="verticalPhoto" x1="0" y1="0" x2="1" y2="1">
            <stop offset="0" stop-color="#f3efe9"/>
            <stop offset="0.5" stop-color="#a9ddd6"/>
            <stop offset="1" stop-color="#cfe7ee"/>
          </linearGradient>
        </defs>
        <polygon points="0,0 220,0 220,200 0,200" fill="url(#verticalPhoto)" role="img" aria-label="Photo of glass jars and flowers on a shop counter"/>
        <polygon points="0,0 55,0 0,80" fill="var(--deep-blue)"/>
        <polygon points="0,80 55,0 80,0 0,120" fill="var(--sky)"/>
        <polygon points="150,70 220,40 220,150" fill="var(--sky)"/>
        <polygon points="0,200 220,200 220,170 0,210" fill="var(--paper)"/>
      </svg>
      <div class="panel__content vertical">
        <h2 class="heading heading--dark">Serving <em>a vertical</em></h2>
        <p class="body-copy">Every industry has its own requirements, traits and characteristics. When you work with clients within a specific industry like retail, you're serving what's known as a vertical market. This means you're supporting the niche requirements of those working in retail stores and businesses with accounting services tailored to their needs. In business, all of the potential purchasers within a business sector, a market which meets the needs of a particular industry by producing similar goods or services.</p>
      </div>
    </div>
  </section>

</div>
</body>
</html>
```